DOVR Business Card Design Project

Company Name: DOVR (Dove Operational Versatile Resources) JLT.
Office Address: Office No 218, Saffron Crest Tower, Palmera Bay Towers, Dubai, U.A.E
Company line of business:
1) Currently we have a POS solution for retail outlets like duty free shops, supermarkets, department stores etc... The solution is deployed in Harbor Gate Retail on 350 POS and in Coralline Port Retail on 100 POS. So our main line of business is the deployment of this solution in retail outlets locally or regionally. We have already deployed the solution in India and Australia.
2) Integration of other third party POS systems with an online credit authorization netwotk in the UAE. This will enable POS applications to connect directly to the acquiring banks without needing an EFT terminal like Paxoline or Tramodex. The credit card payment is completed at the POS.
3) Other solutions that are targeting retail outlets like mobile POS, queue busting solutions, stock taking solutions using hand held devices, transaction capture systems, etc...
4) Other IT services like support of call center solutions from Bramwell Systems and development of new solutions as per customer requirements.
We need a business card design for the company. We don't have any specific requirements and will eave up to the designers to come up with creative designs. At the moment we still don't have a letter head design and the only thing that we have is the company logo that we will upload shortly.
Updates
Dear All,
I just uploaded the logo source files. I am sorry for the delay.
Regards
Tarek Demirci
I would like the business cards to have the following details:
Company Tel No
Company Fax No
Company Website Address
Employee Name
Employee Title
Employee Mobile Number
Employee Email Address

```html
<!DOCTYPE html>
<html lang="en">
<head>
<meta charset="utf-8">
<title>DOVR Business Cards</title>
<link rel="stylesheet" href="https://fonts.googleapis.com/css2?family=Montserrat:wght@500&family=Open+Sans:wght@400;700&display=swap">
<style>
  :root {
    --backdrop: #ebe7e3;
    --card-white: #ffffff;
    --card-edge: #3a3a3a;
    --ink: #111111;
    --ink-soft: #4a4a4a;
    --brand-red: #e01e2c;
    --brand-red-deep: #86293a;
    --brand-blue: #1a6fb8;
    --mark-dot: #e01e2c;
  }
  * { box-sizing: border-box; margin: 0; padding: 0; }
  html, body { width: 1200px; height: 731px; overflow: hidden; }
  body { background: var(--backdrop); position: relative; font-family: "Open Sans", sans-serif; }

  .card {
    position: absolute;
    width: 504px;
    height: 287px;
    border-radius: 24px;
    overflow: hidden;
    border: 1px solid var(--card-edge);
    background: var(--card-white);
  }
  .card--front { left: 60px; top: 219px; border-color: #d8d8d8; }
  .card--back-red {
    left: 627px; top: 51px;
    border: none;
    background: radial-gradient(ellipse 70% 95% at 42% 20%, #ee1f2d 0%, #c4222f 45%, var(--brand-red-deep) 100%);
  }
  .card--back-white { left: 627px; top: 383px; }

  .brand {
    position: absolute;
    display: flex;
    align-items: center;
    gap: 22px;
  }
  .brand__dot {
    width: 64px; height: 64px;
    border-radius: 50%;
    background: var(--mark-dot);
  }
  .brand__name {
    font-family: "Montserrat", sans-serif;
    font-weight: 500;
    font-size: 62px;
    line-height: 1;
    letter-spacing: 1px;
    color: var(--ink);
  }
  .card--front .brand { left: 150px; top: 46px; }
  .card--back-red .brand, .card--back-white .brand { left: 150px; top: 92px; }
  .card--back-red .brand__dot { background: #ffffff; }
  .card--back-red .brand__name { color: #ffffff; }

  .contact {
    position: absolute;
    left: 0; right: 0; top: 158px;
    text-align: center;
    font-size: 12px;
    color: var(--ink-soft);
    line-height: 21px;
  }
  .contact__row { display: flex; justify-content: center; align-items: center; gap: 10px; }
  .contact__item { display: inline-flex; align-items: center; gap: 4px; }
  .contact__icon { width: 10px; height: 10px; fill: var(--ink-soft); }

  .footer-band {
    position: absolute;
    left: 0; right: 0; bottom: 0;
    height: 46px;
    background: linear-gradient(90deg, var(--brand-blue) 0%, #c92131 45%, var(--brand-red) 65%, var(--brand-red-deep) 100%);
  }

  .person {
    position: absolute;
    right: 36px; bottom: 14px;
    color: #ffffff;
    font-size: 12px;
    display: flex; align-items: baseline; gap: 10px;
  }
  .person__name { font-weight: 700; font-size: 15px; }
  .person__divider { opacity: 0.8; }

  .web {
    position: absolute;
    left: 0; right: 0; bottom: 20px;
    text-align: center;
    font-weight: 700;
    font-size: 12px;
    letter-spacing: 2.4px;
  }
  .card--back-red .web { color: #ffffff; }
  .card--back-white .web { color: var(--ink); }
</style>
</head>
<body>

<section class="card card--front" aria-label="Business card front">
  <div class="brand">
    <span class="brand__dot"></span>
    <span class="brand__name">DOVR</span>
  </div>

  <div class="contact">
    <div>Office No 218, Saffron Crest Tower, Palmera Bay Towers, Dubai, U.A.E</div>
    <div class="contact__row">
      <span class="contact__item">
        <svg class="contact__icon" viewBox="0 0 10 10"><path d="M2 0.5 L3.6 2.6 L2.7 3.6 C3.3 5 4.8 6.6 6.3 7.3 L7.4 6.4 L9.5 8 L8.4 9.6 C4.6 9.4 0.6 5.4 0.4 1.6 Z"/></svg>123 456 7890
      </span>
      <span class="contact__item">
        <svg class="contact__icon" viewBox="0 0 10 10"><path d="M3 0 H7 A1 1 0 0 1 8 1 V9 A1 1 0 0 1 7 10 H3 A1 1 0 0 1 2 9 V1 A1 1 0 0 1 3 0 Z M3 1.5 V7 H7 V1.5 Z"/></svg>123 456 7890
      </span>
      <span class="contact__item">
        <svg class="contact__icon" viewBox="0 0 10 10"><path d="M3 0 H7 V3 H9.5 V8 H7.5 V10 H2.5 V8 H0.5 V3 H3 Z M3.5 6.5 V9 H6.5 V6.5 Z"/></svg>123 456 7890
      </span>
    </div>
    <div class="contact__row">
      <span class="contact__item">
        <svg class="contact__icon" viewBox="0 0 10 10"><path d="M0.5 2 H9.5 V8 H0.5 Z"/><path d="M0.5 2 L5 5.5 L9.5 2" fill="none" stroke="#fff" stroke-width="0.9"/></svg>dovr@.com
      </span>
      <span class="contact__item">
        <svg class="contact__icon" viewBox="0 0 10 10"><circle cx="5" cy="5" r="4.5"/><path d="M0.5 5 H9.5 M5 0.5 V9.5 M5 0.5 C2.5 3 2.5 7 5 9.5 M5 0.5 C7.5 3 7.5 7 5 9.5" fill="none" stroke="#fff" stroke-width="0.7"/></svg>www.dovr.com
      </span>
    </div>
  </div>

  <div class="footer-band" role="img" aria-label="Decorative colour wave band in blue, green and red"></div>

  <div class="person">
    <span class="person__name">Name</span>
    <span class="person__divider">|</span>
    <span class="person__title">Title</span>
  </div>
</section>

<section class="card card--back-red" aria-label="Business card back, red">
  <div class="brand">
    <span class="brand__dot"></span>
    <span class="brand__name">DOVR</span>
  </div>
  <div class="web">www.dovr.com</div>
</section>

<section class="card card--back-white" aria-label="Business card back, white">
  <div class="brand">
    <span class="brand__dot"></span>
    <span class="brand__name">DOVR</span>
  </div>
  <div class="web">www.dovr.com</div>
</section>

</body>
</html>
```